A4 Flyer for charity car show

The "Brook Vale Charity Motor Fair" is an annual event that supports a different charity each year. The event aims to aim money and awareness for a cause as well as display a wide range of different cars that are in the community. These include classic cars, muscle cars, exotic cars and many more.

Information to be included:

The event will be held on: 15th of July 2018.
Charity Supported: Proudly supporting Skyward Care Australia
Location: Renwick Oval, Dorrigal
Website: http://www.brookvalemotorfair.com.au/

Target Market(s)

Car enthusiasts, professionals

Industry/Entity Type

Charity

Requirements
Must have
• Any car used in the flyer must look like they are in a field. Cars used must be right hand drive.

```html
<!DOCTYPE html>
<html lang="en">
<head>
<meta charset="utf-8">
<title>Brook Vale Charity Motor Fair — Flyer</title>
<link rel="stylesheet" href="https://fonts.googleapis.com/css2?family=Bebas+Neue&family=Montserrat:wght@400;500&family=Playfair+Display:ital@1&display=swap">
<style>
  :root {
    --backdrop: #e6e1d9;
    --cream: #f7e8d3;
    --brown: #5b3618;
    --ink: #2a1a0e;
    --rule: #a98c70;
    --pin: #9a7b66;
    --white: #ffffff;
    --logo-blue: #203a5c;
  }
  * { margin: 0; padding: 0; box-sizing: border-box; }
  html, body { width: 1200px; height: 1200px; overflow: hidden; }
  body { background: var(--backdrop); position: relative; }

  .flyer {
    position: absolute; left: 77px; top: 17px;
    width: 1046px; height: 1166px;
    background: var(--cream);
    overflow: hidden;
  }
  .hero {
    position: absolute; left: 0; top: 0; width: 1046px; height: 561px;
    background:
      radial-gradient(ellipse 45% 55% at 50% 55%, #9a1f2c 0%, #6e1420 45%, transparent 75%),
      linear-gradient(180deg, #2f3b24 0%, #3d5a2a 35%, #2f4a22 70%, #161c12 100%);
  }
  .hero-shade { position: absolute; inset: 0; background: rgba(20, 10, 10, 0.25); }

  .line { position: absolute; left: 0; right: 0; text-align: center; white-space: nowrap; }

  .title-the {
    top: 180px; height: 54px; line-height: 54px;
    font-family: "Playfair Display", serif; font-style: italic;
    font-size: 45px; color: var(--white);
  }
  .title-name {
    top: 232px; height: 68px; line-height: 68px;
    font-family: "Bebas Neue", sans-serif; font-size: 68px;
    letter-spacing: 0.24em; padding-left: 0.24em; color: var(--white);
  }
  .title-main {
    top: 305px; height: 164px; line-height: 164px;
    font-family: "Bebas Neue", sans-serif; font-size: 170px;
    letter-spacing: 0.14em; padding-left: 0.14em; color: var(--white);
  }

  .event-label {
    top: 613px; height: 24px; line-height: 24px;
    font-family: "Montserrat", sans-serif; font-weight: 500;
    font-size: 16px; letter-spacing: 0.3em; padding-left: 0.3em; color: var(--brown);
  }
  .event-date {
    top: 652px; height: 66px; line-height: 66px;
    font-family: "Bebas Neue", sans-serif; font-size: 68px;
    letter-spacing: 0.09em; color: var(--brown);
  }
  .event-date sup {
    font-family: "Playfair Display", serif; font-style: italic;
    font-size: 30px; letter-spacing: 0; vertical-align: 28px; line-height: 0; margin-right: 8px;
  }
  .rule { position: absolute; background: var(--rule); }
  .rule-top { left: 162px; width: 725px; top: 743px; height: 1px; }

  .charity {
    top: 772px; height: 28px; line-height: 28px;
    font-family: "Bebas Neue", sans-serif; font-size: 24px;
    letter-spacing: 0.09em; color: var(--ink);
  }
  .pin { position: absolute; left: 503px; top: 826px; width: 40px; height: 50px; }
  .location {
    top: 892px; height: 60px; line-height: 60px;
    font-family: "Bebas Neue", sans-serif; font-size: 58px;
    letter-spacing: 0.07em; color: var(--brown);
  }

  .rule-footer-top { left: 162px; width: 725px; top: 1011px; height: 1px; }
  .rule-footer-bottom { left: 162px; width: 725px; top: 1110px; height: 1px; }
  .rule-footer-split { left: 522px; width: 1px; top: 989px; height: 131px; }

  .brand {
    position: absolute; left: 162px; width: 360px; top: 1011px; height: 99px;
    display: flex; align-items: center; justify-content: center; gap: 12px;
  }
  .brand-dot { width: 22px; height: 22px; border-radius: 50%; background: var(--logo-blue); }
  .brand-name {
    font-family: "Montserrat", sans-serif; font-weight: 500;
    font-size: 17px; letter-spacing: 0.06em; color: var(--logo-blue); white-space: nowrap;
  }
  .website {
    position: absolute; left: 522px; width: 365px; top: 1011px; height: 99px;
    display: flex; align-items: center; justify-content: center;
    font-family: "Montserrat", sans-serif; font-size: 14.5px;
    letter-spacing: 0.04em; color: var(--brown); white-space: nowrap;
  }
</style>
</head>
<body>
  <main class="flyer">
    <div class="hero" role="img" aria-label="Photo of a red vintage right-hand-drive roadster parked on a grass field at the show">
      <div class="hero-shade"></div>
    </div>
    <p class="line title-the">the</p>
    <h1 class="line title-name">BROOK VALE CHARITY</h1>
    <p class="line title-main">MOTOR FAIR</p>

    <p class="line event-label">THE EVENT WILL BE HELD ON</p>
    <p class="line event-date">15<sup>th</sup>OF JULY 2018</p>
    <div class="rule rule-top"></div>

    <p class="line charity">CHARITY SUPPORTED:PROUDLY SUPPORTING SKYWARD CARE AUSTRALIA</p>

    <svg class="pin" viewBox="0 0 40 50" aria-hidden="true">
      <path d="M20 2C10 2 3 9.5 3 19c0 12 17 29 17 29s17-17 17-29C37 9.5 30 2 20 2z" fill="var(--pin)"/>
      <circle cx="20" cy="19" r="7" fill="var(--cream)"/>
    </svg>
    <p class="line location">RENWICK OVAL, DORRIGAL</p>

    <div class="rule rule-footer-top"></div>
    <div class="rule rule-footer-bottom"></div>
    <div class="rule rule-footer-split"></div>

    <div class="brand">
      <span class="brand-dot"></span>
      <span class="brand-name">Brook Vale Motor Fair</span>
    </div>
    <div class="website">http://www.brookvalemotorfair.com.au/</div>
  </main>
</body>
</html>
```